Leaflet to promote a new sports massage business

I am a Remedial and Sports Massage therapist and treat a range of people from professionals who spend hours working behind computers and have associated neck and back pain through poor posture to amateur sports people of varying intensity/ability - who encounter injuries along the way, or just need some good old stretching out.Remedial and sports massage helps people who have musculoskeletal injury, pain or dysfunction brought about by the stresses and strains of life. Through massage i can reduce pain, promote recovery after injury, relieve stress, and improve flexibility. All of this contributes to helping people feel better. I have just started working at a new location (address attached) and am looking to raise awareness that I am there and to promote the benefits of massage to encourage new clients(attached as a separate document). I have a business card (attached to the brief) which uses hands as the main device, I would like to include these – possibly in some sort of logo and I would like to use purple as a key colour (if colour is used). I also want to include the KVTB logo (attached) to add credibility

```html
<!DOCTYPE html>
<html lang="en">
<head>
<meta charset="utf-8">
<title>Helena Marsh – Remedial and Sports Massage</title>
<link href="https://fonts.googleapis.com/css2?family=Oswald:wght@600&family=Open+Sans:wght@400;600&family=Raleway:wght@300;400&display=swap" rel="stylesheet">
<style>
  :root {
    --purple: #6b1f5f;
    --purple-dark: #561a4c;
    --white: #ffffff;
    --grey: #5a5a5a;
    --skin-light: #efe4d8;
    --skin-mid: #d9b9a0;
    --page: #ffffff;
  }
  * { margin: 0; padding: 0; box-sizing: border-box; }
  html, body { width: 769px; height: 1200px; overflow: hidden; background: var(--page); }
  .leaflet { position: relative; width: 769px; height: 1200px; font-family: "Open Sans", Arial, sans-serif; }

  .hero-photo {
    position: absolute; left: 0; top: 0; width: 769px; height: 546px;
    background: linear-gradient(160deg, var(--skin-light) 0%, #e8d3c2 45%, var(--skin-mid) 75%, #b99a88 100%);
  }

  .benefits {
    position: absolute; left: 0; top: 546px; width: 769px; height: 370px;
    background: var(--purple); color: var(--white); text-align: center;
  }
  .benefits-heading {
    display: flex; align-items: center; justify-content: center; gap: 22px;
    margin-top: 30px;
    font-family: "Oswald", "Arial Narrow", sans-serif; font-weight: 600;
    font-size: 40px; letter-spacing: 1px; line-height: 1;
  }
  .rule { width: 130px; height: 14px; border-top: 4px solid var(--white); border-bottom: 4px solid var(--white); }
  .benefit-list { list-style: none; margin-top: 26px; }
  .benefit-list li {
    display: flex; align-items: center; justify-content: center; gap: 12px;
    font-size: 27px; line-height: 1; margin-bottom: 22px;
  }
  .tick-box { width: 24px; height: 24px; flex: none; }

  .contact {
    position: absolute; left: 0; top: 916px; width: 769px; height: 284px; background: var(--white);
  }
  .hands-mark {
    position: absolute; left: 20px; top: 30px; width: 280px; height: 254px;
    background: linear-gradient(135deg, #8a3a7c 0%, var(--purple) 55%, var(--purple-dark) 100%);
    border-radius: 60px 60px 0 0;
  }
  .contact-details {
    position: absolute; left: 308px; top: 14px; width: 455px; text-align: center; color: var(--purple);
  }
  .therapist-name { font-family: "Raleway", Arial, sans-serif; font-weight: 400; font-size: 44px; letter-spacing: 1px; line-height: 1.1; }
  .therapist-role { font-family: "Raleway", Arial, sans-serif; font-weight: 400; font-size: 22px; line-height: 1.25; white-space: nowrap; }
  .practice { color: var(--grey); font-size: 17px; line-height: 1.3; margin-top: 6px; }
  .address { color: var(--grey); font-size: 17px; line-height: 1.3; margin-top: 8px; }
  .contact-lines { list-style: none; margin-top: 10px; color: var(--grey); font-size: 17px; }
  .contact-lines li { display: flex; align-items: center; justify-content: center; gap: 10px; margin-bottom: 7px; line-height: 1; }
  .contact-icon { width: 20px; height: 20px; flex: none; }
</style>
</head>
<body>
<main class="leaflet">
  <div class="hero-photo" role="img" aria-label="Photograph of a therapist massaging a client's leg on a treatment couch"></div>

  <section class="benefits">
    <h1 class="benefits-heading"><span class="rule"></span>BENEFITS OF MASSAGE<span class="rule"></span></h1>
    <ul class="benefit-list">
      <li><svg class="tick-box" viewBox="0 0 24 24"><rect x="1.5" y="3.5" width="19" height="19" fill="none" stroke="#fff" stroke-width="2.5"/><path d="M5 12l5 6L23 2" fill="none" stroke="#fff" stroke-width="3"/></svg>Reduces Pain</li>
      <li><svg class="tick-box" viewBox="0 0 24 24"><rect x="1.5" y="3.5" width="19" height="19" fill="none" stroke="#fff" stroke-width="2.5"/><path d="M5 12l5 6L23 2" fill="none" stroke="#fff" stroke-width="3"/></svg>Promotes Recovery</li>
      <li><svg class="tick-box" viewBox="0 0 24 24"><rect x="1.5" y="3.5" width="19" height="19" fill="none" stroke="#fff" stroke-width="2.5"/><path d="M5 12l5 6L23 2" fill="none" stroke="#fff" stroke-width="3"/></svg>Improves Posture and Flexibility</li>
      <li><svg class="tick-box" viewBox="0 0 24 24"><rect x="1.5" y="3.5" width="19" height="19" fill="none" stroke="#fff" stroke-width="2.5"/><path d="M5 12l5 6L23 2" fill="none" stroke="#fff" stroke-width="3"/></svg>Relieves Stress</li>
      <li><svg class="tick-box" viewBox="0 0 24 24"><rect x="1.5" y="3.5" width="19" height="19" fill="none" stroke="#fff" stroke-width="2.5"/><path d="M5 12l5 6L23 2" fill="none" stroke="#fff" stroke-width="3"/></svg>Improves Health and Wellbeing</li>
    </ul>
  </section>

  <footer class="contact">
    <div class="hands-mark" role="img" aria-label="Purple hands emblem of the massage practice"></div>
    <div class="contact-details">
      <h2 class="therapist-name">HELENA MARSH</h2>
      <p class="therapist-role">Remedial and Sports Massage Therapist</p>
      <p class="practice">Peak Motion Physiotherapy</p>
      <p class="address">Westbrook Athletic Ground<br>Mill Lane Road, Westbrook, WB4 7QT</p>
      <ul class="contact-lines">
        <li><svg class="contact-icon" viewBox="0 0 22 22"><circle cx="11" cy="11" r="11" fill="#6b1f5f"/><path d="M8 5.5c-.8 0-1.8 1-1.6 2.4.5 3.4 3.6 7 7.4 8.2 1.3.4 2.4-.4 2.6-1.3l-2.2-1.6-1.2 1c-1.7-.8-3.2-2.4-3.8-4.1l1-1.1z" fill="#fff"/></svg>07700 900123</li>
        <li><svg class="contact-icon" viewBox="0 0 22 22"><rect x="2" y="5" width="18" height="12" rx="1" fill="none" stroke="#6b1f5f" stroke-width="1.8"/><path d="M2.5 5.5L11 12l8.5-6.5" fill="none" stroke="#6b1f5f" stroke-width="1.8"/></svg>helenamarsh@mailbox.com</li>
        <li><svg class="contact-icon" viewBox="0 0 22 22"><circle cx="11" cy="11" r="11" fill="#6b1f5f"/></svg>social/HelenaMarshMassage</li>
      </ul>
    </div>
  </footer>
</main>
</body>
</html>
```